Wordpress website design for a Herbal Health Care Company

** Outcome of this project is only the design. Only PSD files of the design for unique pages are sufficient.
** There are a number of unique pages in the new site as shown in the wire-frame. However, for the selection of the designer, Homepage, one 2nd tier page (product category) and one 3rd tier page (product page) is sufficient.
We need web design for our for Ayurvedic & Herbal Products Company located in Sri Lanka
Please get the idea about our company by reading the following text
Vision : To be a world class manufacturer and a supplier of highest quality Ayurvedic pharmaceuticals, Herbal health care products, Herbal cosmetics, Essential oils and Oleoresins
Mission : To provide safe and effective Ayurvedic pharmaceuticals, Herbal health care products and Herbal cosmetics, that is of highest quality and integrity, through the incorporation of ancient ayurvedic wisdom with modern technology and scientific management systems for the inprovement of health and longevity of the people.
Policy on Quality : To design, develop, produce and deliver safe, efficacious and consistent quality Herbal health care products based on Ancient Ayurvedic Wisdom using environmentally preferred process technologies and competent personnel towards continual commitment to total customer satisfaction.
(1) Color theme of the website
You can use the color derived from the company logo
(2) Site Map and description of the site
(1) Home
see the wire frame
http://clipvault.example/t/qRtMnWpLs4kX
we need drop-down menu for top menu bar
(2) About Velora Botanics [ This is single page with some description + imaged and following sub page links should be placed in this page]
2.1 Board of Directors
2.2 Milestones
2.3 Our Logo
2.4 Production & R&D
2.5 Certification and Awards
2.6 Global Presence
2.7 Investors
2.8 Distribution
(3)Ayurveda Pharmaceuticals [ This is one of the 3 main categories ,Category Main Page should provide an introduction to the category]
Following shows the sub categories of the “Ayurvedic Pharmaceuticals” . each subcategory has different products. We need unique design for Main Category Page and Sub category
3.1 Arista
3.2 Asava
3.3 Coorna
3.4 Lepa
3.5 Gritha
3.7 Guggulu
3.8 Kalka
3.9 Kwatha
3.10 Pana
see the wireframe
http://clipvault.example/t/7JwoKd31RTBB
when you click subcategory , we nee a page like this to list products
http://clipvault.example/t/HNmVx5Qe82
(4) Herbal Health Care Products [ This is one of the 3 main categories]
you do not find subcategories, you have only products listed. we need unique design for this category page + products
This page will consists of category description with image and products listed
see the wire frame
(5) Cosmetics & Spa Products
see the wire frame
(6) Essential Oils & Oleoresins
see the wire frame
(7) Media
We need to put video / image gallery / text . and future events
(8) Investors
related information to investors
we need image + text
(9) CSR
(10) Contact US
contact us form / address / telephone number and google map
(11) Log In
Normal login form
(12) Career
Reference Details
http://clipvault.example/t/2PfRoLT9GWM
http://clipvault.example/t/8KyvHMM4Rd
http://clipvault.example/t/bQeFxNRtt
Here is a similar site that should give you some idea how we like the new site to look http://www.veronix.example
Industry/Entity Type
Health Care
Requirements
Must have
- We have 4 main categories in our production line
Quality Ayurvedic pharmaceuticals, Herbal health care products, Herbal cosmetics, Essential oils and Oleoresins
You can use 4 boxes below the slider for it ( This very important to have unique different design for each category with some heading, text and images etc)
Nice to have
- You can suggest any good nice features. Try to keep a clean, natural, relaxing theme, with shades of green, white and orange as per their logo. This can be seen from the project brief attachments. www.veronix.example is an example.
Should not have
- Please avoid dark colours (red) and sad colours (grey, black)

```html
<!DOCTYPE html>
<html lang="en">
<head>
<meta charset="utf-8">
<title>Velora Botanics – Home</title>
<link href="https://fonts.googleapis.com/css2?family=Arimo:ital,wght@0,400;0,700;1,400;1,700&display=swap" rel="stylesheet">
<style>
:root{
  --green:#2fa464;
  --green-dark:#1f8a4f;
  --green-band:#3bb172;
  --leaf:#5a9a2e;
  --leaf-light:#a6cf6a;
  --yellow:#fcc419;
  --yellow-deep:#f6b40e;
  --orange:#f28a0c;
  --text:#222;
  --grey-bar:#a9a9a9;
  --white:#fff;
}
*{box-sizing:border-box;margin:0;padding:0}
html,body{width:1200px;height:900px;overflow:hidden;background:var(--white)}
body{position:relative;font-family:"Arimo",Arial,sans-serif;color:var(--text)}
.abs{position:absolute}
.brand{left:322px;top:17px;width:72px;height:47px;border:2px solid var(--green);border-radius:3px;display:flex;align-items:center;justify-content:center;text-align:center;color:var(--green);font-weight:700;font-size:11px;line-height:12px}
.util-nav{right:314px;top:22px;font-size:9px;color:var(--green);font-variant:small-caps;font-weight:700;letter-spacing:.3px}
.util-nav span{margin:0 4px}
.search-field{left:735px;top:50px;width:107px;height:17px;border:1px solid #cfe8d8;border-radius:2px}
.search-btn{left:847px;top:50px;width:39px;height:17px;background:var(--yellow);color:var(--white);font-size:7px;font-weight:700;display:flex;align-items:center;justify-content:center;border-radius:2px}
.main-nav{left:318px;top:82px;width:568px;display:flex;justify-content:space-between;font-size:8.3px;color:var(--green);font-variant:small-caps;font-weight:700;white-space:nowrap}
.main-nav .current{color:var(--orange)}
.main-nav i{font-style:normal}
.slider{left:319px;top:107px;width:561px;height:162px;border:2px solid var(--green);border-radius:3px;overflow:hidden;box-shadow:0 1px 3px rgba(0,0,0,.25)}
.slide-photo{position:absolute;left:27px;top:18px;width:212px;height:124px;background:linear-gradient(180deg,#fbfbf9 0%,#f1f3ee 40%,#b9d39a 72%,#4f8f2e 100%)}
.slide-title{position:absolute;left:392px;top:60px;font-size:14px;letter-spacing:1.5px;color:var(--green)}
.slide-bar{position:absolute;left:0;bottom:0;width:100%;height:18px;background:var(--grey-bar)}
.dot{position:absolute;top:3px;width:12px;height:12px;border-radius:50%;background:var(--green);border:1.5px solid var(--white)}
.categories{left:312px;top:292px;width:575px;height:106px;background:var(--yellow)}
.cat-tile{position:absolute;top:5px;width:132px;height:96px;border:3px solid var(--yellow-deep);background:var(--white);padding:1px}
.cat-tile div{width:100%;height:100%}
.about-title{left:331px;top:420px;font-size:13px;font-style:italic;font-weight:700;font-variant:small-caps;color:var(--orange);letter-spacing:.5px}
.about-body{left:325px;top:443px;width:403px;font-size:7.6px;line-height:9.2px;text-align:justify}
.about-body p{margin-bottom:9px}
.about-body .link{color:var(--orange);font-style:italic;text-decoration:underline}
.about-body blockquote{margin-left:12px}
.read-more{left:646px;top:596px;font-size:10px;color:var(--orange)}
.sidebar-head{font-size:9.5px;color:var(--orange)}
.sub-field{left:752px;top:444px;width:93px;height:16px;border:2px solid #c9c9c9;border-radius:3px}
.sub-go{left:852px;top:444px;width:27px;height:16px;background:#555;color:var(--orange);font-size:11px;display:flex;align-items:center;justify-content:center}
.avatar{position:absolute;left:751px;width:20px;height:20px;background:#1e1e1e;border-radius:50% 50% 3px 3px}
.testimonial{position:absolute;left:781px;width:100px;font-size:7.2px;line-height:8.8px;color:var(--orange);text-align:justify}
.testimonial u{color:var(--text)}
.blog-link{left:788px;top:597px;font-size:9.5px;font-style:italic;color:var(--text);display:flex;align-items:center;gap:6px}
.gallery{left:317px;top:654px;width:565px;height:107px;background:linear-gradient(180deg,var(--green-band) 0%,#5cc48a 50%,var(--green-band) 100%);border:1px solid #cfd8d2}
.thumb{position:absolute;top:24px;width:60px;height:60px;border:2px solid #2e9a5e;background:var(--white);padding:3px}
.thumb div{width:100%;height:100%;background:linear-gradient(180deg,#f6f8f3 0%,#6fae45 35%,#3f8a2a 55%,#e4e2dc 78%,#f4f4f2 100%)}
.arrow{position:absolute;top:35px}
.footer-rule{left:294px;top:773px;width:612px;height:6px;background:var(--green-band)}
.footer{left:294px;top:779px;width:612px;height:121px;background:var(--yellow)}
.footer-head{position:absolute;top:14px;font-size:9.5px;font-style:italic;color:var(--green)}
.footer-line{position:absolute;left:29px;top:26px;width:558px;height:1px;background:#e0a910}
.footer-col{position:absolute;font-size:7.4px;line-height:8.6px}
.footer-col .g{color:var(--green)}
.footer-col .t{color:#333;font-size:6px}
.map{position:absolute;left:303px;top:36px;width:104px;height:76px;background:linear-gradient(135deg,#eceee8,#dfe3da);border:1px solid #ccc}
</style>
</head>
<body>

<header>
  <div class="abs brand">Velora<br>Botanics</div>
  <nav class="abs util-nav">Media<span>|</span>Investors<span>|</span>Careers<span>|</span>CSR<span>|</span>Contact Us<span>|</span>Log in</nav>
  <div class="abs search-field"></div>
  <div class="abs search-btn">SEARCH</div>
  <nav class="abs main-nav">
    <span class="current">Home</span><i>|</i>
    <span>About Velora Botanics</span><i>|</i>
    <span>Ayurvedic Pharmaceuticals</span><i>|</i>
    <span>Herbal Health Care</span><i>|</i>
    <span>Products Cosmetics &amp; Spa products</span><i>|</i>
    <span>Essential Oils</span>
  </nav>
</header>

<section class="abs slider">
  <div class="slide-photo" role="img" aria-label="Marble mortar and pestle with fresh green herbs"></div>
  <div class="slide-title">VELORA BOTANICS</div>
  <div class="slide-bar">
    <span class="dot" style="left:482px"></span>
    <span class="dot" style="left:503px"></span>
    <span class="dot" style="left:524px;background:var(--green-dark)"></span>
  </div>
</section>

<section class="abs categories">
  <div class="cat-tile" style="left:9px"><div role="img" aria-label="Close-up of green clover leaves" style="background:linear-gradient(160deg,var(--leaf-light) 0%,#86b84a 50%,var(--leaf) 100%)"></div></div>
  <div class="cat-tile" style="left:152px"><div role="img" aria-label="Feathery fern fronds in a pot" style="background:linear-gradient(180deg,#eef2ea 0%,#a9c99a 45%,#7fae6a 70%,#e8ece4 100%)"></div></div>
  <div class="cat-tile" style="left:295px"><div role="img" aria-label="Herbs with garlic and mortar" style="background:linear-gradient(180deg,#fafbf8 0%,#6fae45 35%,#3f8a2a 55%,#e4e2dc 80%,#fafafa 100%)"></div></div>
  <div class="cat-tile" style="left:438px"><div role="img" aria-label="Sprig of fresh parsley" style="background:linear-gradient(180deg,#fff 0%,#8cc35a 35%,#3d8f27 65%,#fff 100%)"></div></div>
</section>

<main>
  <h1 class="abs about-title">About Velora Botanics</h1>
  <div class="abs about-body">
    <p>Pellentesque habitant morbi tristique senectus et netus et malesuada fames ac turpis egestas. Vestibulum tortor quam, feugiat vitae, ultricies eget, tempor sit amet, ante. Donec eu libero sit amet quam egestas semper. Aenean ultricies mi vitae est. Mauris placerat eleifend leo. Quisque sit amet est et sapien ullamcorper pharetra. Vestibulum erat wisi, condimentum sed, commodo vitae, ornare sit amet, wisi. Aenean fermentum, elit eget tincidunt condimentum, eros ipsum rutrum orci, sagittis tempus lacus enim ac dui. Donec non enim in turpis pulvinar facilisis. Ut felis. Praesent dapibus, neque id cursus faucibus, tortor neque egestas augue, eu vulputate magna eros eu erat. Aliquam erat volutpat. Nam dui mi, tincidunt <span class="link">quis</span>, accumsan porttitor, facilisis luctus, metus.</p>
    <p>Pellentesque habitant morbi tristique senectus et netus et malesuada fames ac turpis egestas. Vestibulum tortor quam, feugiat vitae, ultricies eget, tempor sit amet, ante. Donec eu libero <span class="link">sit amet quam</span> egestas semper. Aenean ultricies mi vitae est. Mauris placerat eleifend leo.</p>
    <blockquote>Consectetur adipisicing elit, sed do eiusmod tempor incididunt ut labore et dolore magna aliqua. Ut enim ad minim veniam, quis nostrud exercitation ullamco laboris nisi ut aliquip ex ea commodo consequat.</blockquote>
  </div>
  <a class="abs read-more">Read More...</a>
</main>

<aside>
  <div class="abs sidebar-head" style="left:751px;top:427px">Subscribe Via E-Mail</div>
  <div class="abs sub-field"></div>
  <div class="abs sub-go">Go</div>
  <div class="abs sidebar-head" style="left:754px;top:467px">Testimonials</div>
  <div class="avatar" style="top:487px" role="img" aria-label="Customer avatar silhouette"></div>
  <p class="testimonial" style="top:483px">Lorem ipsum dolor sit amet, consectetuer adipiscing elit, sed diam nonummy .</p>
  <div class="avatar" style="top:524px" role="img" aria-label="Customer avatar silhouette"></div>
  <p class="testimonial" style="top:521px">Lorem ipsum dolor sit amet, consectetuer adipiscing elit, sed diam <u>nonummy</u> .</p>
  <div class="avatar" style="top:560px" role="img" aria-label="Customer avatar silhouette"></div>
  <p class="testimonial" style="top:557px">Lorem ipsum dolor sit amet, consectetuer <u>adipiscing</u> elit, sed diam nonummy .</p>
  <div class="abs blog-link">
    <svg width="8" height="6" viewBox="0 0 8 6"><path d="M0 0 L8 3 L4 6 Z" fill="#f28a0c"/></svg>
    Velora Botanics Blog
  </div>
</aside>

<section class="abs gallery">
  <svg class="arrow" style="left:24px" width="16" height="34" viewBox="0 0 16 34"><path d="M14 2 L2 17 L14 32" fill="none" stroke="#fff" stroke-width="3"/></svg>
  <svg class="arrow" style="left:524px" width="16" height="34" viewBox="0 0 16 34"><path d="M2 2 L14 17 L2 32" fill="none" stroke="#fff" stroke-width="3"/></svg>
  <div class="thumb" style="left:75px"><div role="img" aria-label="Herbs with garlic and mortar"></div></div>
  <div class="thumb" style="left:148px"><div role="img" aria-label="Herbs with garlic and mortar"></div></div>
  <div class="thumb" style="left:219px"><div role="img" aria-label="Herbs with garlic and mortar"></div></div>
  <div class="thumb" style="left:290px"><div role="img" aria-label="Herbs with garlic and mortar"></div></div>
  <div class="thumb" style="left:362px"><div role="img" aria-label="Herbs with garlic and mortar"></div></div>
  <div class="thumb" style="left:433px"><div role="img" aria-label="Herbs with garlic and mortar"></div></div>
</section>

<div class="abs footer-rule"></div>
<footer class="abs footer">
  <div class="footer-head" style="left:29px">Lates Blog Posts</div>
  <div class="footer-head" style="left:217px">Contact Details</div>
  <div class="footer-head" style="left:413px;font-style:normal">Social Feeds</div>
  <div class="footer-line"></div>

  <div class="footer-col" style="left:24px;top:35px;width:172px">
    <p>Consectetur adipisicing elit</p>
    <p class="g" style="margin:2px 0 10px 6px">Eodem modo typi, qui nunc nobis videntur parum clari, fiant sollemnes in futurum.</p>
    <p>Consectetur adipisicing elit</p>
    <p class="g" style="margin:2px 0 0 6px">Investigationes demonstraverunt lectores legere me lius quod ii legunt saepius.</p>
  </div>

  <div class="footer-col" style="left:209px;top:44px;width:88px">
    <p>Adress:<span class="g">42 Fernleaf Road, 2nd Floor, Kandy 20000</span></p>
    <p style="margin-top:9px">Phone: <span class="g">+94 81-555-0140</span></p>
    <p>Fax: &nbsp;&nbsp;&nbsp;<span class="g">+94 81-555-0141</span></p>
  </div>
  <div class="map" role="img" aria-label="Street map showing the office location"></div>

  <div class="footer-col" style="left:420px;top:30px;width:186px">
    <p>Ravi Perin</p>
    <p style="margin-top:3px"><span class="g">UT</span> @ testpage: <span class="g">Eprehenderit in voluptate velit! (Esse cillum dolore eu fugiat nulla pariatur!)...</span></p>
    <p class="t" style="margin:2px 0 8px 6px">4 hours ago</p>
    <p>Mala Sena</p>
    <p class="g" style="margin-top:3px">Ut enim ad minim veniam, quis nostrud exercitation #ullamco laboris nisi ut aliquip ex ea commodo consequat. <span class="t">6 hours ago</span></p>
  </div>
</footer>

</body>
</html>
```